MAPLE Quarters One-Page Inserts

We need TWO one-page insert for a transplant display stand (6"x8"). We have a few furnished apartments and we need to inform our guests about the services available:

Insert #1: Delivery and Pickup Services in the neighborhood (Laundry, Groceries, Restaurants).
Insert #1 Text: "Heading: Pick and Delivery Services in your neighborhood:" Text below it: "1) Laundry Pickup - Call: +9714-382-6047. 2) Groceries Delivery - Call: +9714-382-6047, 3) Restaurants Delivery - Call: +9714-382-6047"

Insert #2: We also need another one-page insert to encourage the guests to enjoy the candles and to make the apartment have a homier feeling.
Insert #2 Text: "Heading: Feel at home. Text below it: "Dim the lights, light up a candle, play nice music, have a relaxing stay."

Target Market(s)

Staynook Users. Apartment Guests. Tourist. Age Group 20 to 60 years old.

Industry/Entity Type

Hotel

Requirements
Must have
• - The Company logo of MAPLE Quarters must be displayed on the upper corner. (Logo attached). The logo should be a single color either white or black (Not red and black or red and white)
• For Insert # 1: Laundry, Groceries, and Breakfast Resturaunts images or icons. The images/icons must be unified and look like from the same family of images/icons.
• For Insert # 2: A romantic candle(s) dinner pictures.
Nice to have
• Not too many colors
• Not too busy
• Simple
• Eye Catchy
Should not have
• Lots of colors
• Too many images
• Too Busy

```html
<!DOCTYPE html>
<html lang="en">
<head>
<meta charset="utf-8">
<title>MAPLE Quarters – Guest Inserts</title>
<link href="https://fonts.googleapis.com/css2?family=Open+Sans:ital,wght@0,400;0,600;0,700;1,400;1,600&family=Pinyon+Script&display=swap" rel="stylesheet">
<style>
  :root {
    --page-bg: #e4e4e6;
    --red: #e8333a;
    --yellow: #fec82b;
    --blue: #0c96d8;
    --white: #ffffff;
    --ink: #2f2f33;
    --pink: #e8388a;
    --script-pink: #f0479a;
    --quote-band: rgba(160, 50, 150, 0.62);
    --icon-ring: #d9d9de;
  }
  * { box-sizing: border-box; margin: 0; padding: 0; }
  html, body { width: 1200px; height: 1200px; overflow: hidden; }
  body {
    background: var(--page-bg);
    font-family: "Open Sans", Arial, sans-serif;
    position: relative;
  }
  .insert {
    position: absolute;
    width: 714px;
    height: 536px;
    overflow: hidden;
  }
  .insert--services { left: 81px; top: 42px; background: var(--blue); }
  .insert--home { left: 385px; top: 615px; background: #1e1418; }

  .contact-bar {
    height: 42px;
    display: flex;
    justify-content: space-between;
    align-items: center;
    padding: 0 33px 0 43px;
    color: var(--white);
    font-size: 13px;
    font-weight: 600;
    font-style: italic;
  }
  .insert--services .contact-bar { background: var(--red); }
  .insert--home .contact-bar { background: linear-gradient(90deg, #e94b57, var(--pink)); }

  .brand {
    position: absolute;
    text-align: center;
    font-family: "Open Sans", Arial, sans-serif;
    font-weight: 600;
    line-height: 1.05;
    font-size: 22px;
  }
  .brand small { display: block; font-size: 13px; letter-spacing: 0.5px; }
  .brand--dark { color: var(--ink); right: 34px; top: 100px; }
  .brand--light { color: var(--white); right: 34px; top: 80px; }

  .headline-band {
    height: 146px;
    background: var(--yellow);
    position: relative;
  }
  .headline {
    position: absolute;
    left: 42px;
    top: 26px;
    color: #fff9ea;
    font-size: 40px;
    font-weight: 600;
    line-height: 52px;
    text-shadow: 2px 3px 3px rgba(120, 80, 0, 0.55);
  }
  .photo-strip { display: flex; height: 184px; }
  .photo-strip .photo { flex: 1; }
  .photo--laundry { background: linear-gradient(135deg, #3ba3e0, #a9d7f0 55%, #e98cb4); }
  .photo--groceries { background: linear-gradient(160deg, #e9e9e9, #d8452f 45%, #7fae3c 75%, #b89a6a); }
  .photo--restaurant { background: linear-gradient(160deg, #b9b3ad, #d8262f 50%, #c98a6c); }

  .services { display: flex; position: relative; height: 163px; }
  .service { flex: 1; position: relative; text-align: center; color: var(--white); }
  .service-icon {
    position: absolute;
    left: 50%;
    top: -50px;
    width: 96px;
    height: 96px;
    margin-left: -48px;
    border-radius: 50%;
    background: var(--white);
    border: 3px solid var(--icon-ring);
    display: flex;
    align-items: center;
    justify-content: center;
  }
  .service-icon span { width: 56px; height: 56px; border-radius: 50%; }
  .icon--laundry span { background: #a7559f; }
  .icon--groceries span { background: linear-gradient(135deg, #e84a3a, #f39a2a 50%, #7a7a7a); }
  .icon--restaurant span { background: linear-gradient(135deg, #f08a2a, #3b2e44); }
  .service-name { position: absolute; left: 0; right: 0; top: 88px; font-size: 19px; font-weight: 600; }
  .service-phone { position: absolute; left: 0; right: 0; top: 114px; font-size: 19px; }

  .mood-photo {
    position: absolute;
    left: 0; top: 42px; right: 0; bottom: 0;
    background:
      radial-gradient(circle at 32% 60%, rgba(255, 150, 90, 0.85), rgba(200, 70, 60, 0.4) 22%, transparent 45%),
      radial-gradient(circle at 85% 45%, rgba(190, 80, 120, 0.8), transparent 40%),
      linear-gradient(160deg, #2a1c20, #4a2a30 50%, #2a1a22);
  }
  .script-title {
    position: absolute;
    right: 80px;
    top: 190px;
    font-family: "Pinyon Script", cursive;
    color: var(--script-pink);
    font-size: 74px;
    line-height: 60px;
    text-shadow: 1px 1px 2px rgba(80, 0, 40, 0.5);
  }
  .script-title .line2 { display: block; padding-left: 120px; }
  .quote-band {
    position: absolute;
    left: 0; right: 0;
    top: 345px;
    height: 112px;
    background: var(--quote-band);
    color: var(--white);
    font-style: italic;
    font-size: 30px;
    line-height: 42px;
    text-align: center;
    padding-top: 14px;
    padding-left: 50px;
  }
</style>
</head>
<body>

<section class="insert insert--services">
  <div class="contact-bar"><span>Call Us 12345 48213</span><span>www.maplequarters.com</span></div>
  <header class="headline-band">
    <h1 class="headline">Pick and Delivery Services<br>in your neighborhood</h1>
    <div class="brand brand--dark">MAPLE<small>QUARTERS</small></div>
  </header>
  <div class="photo-strip">
    <div class="photo photo--laundry" role="img" aria-label="Photo of a clothes iron beside a stack of folded colourful laundry"></div>
    <div class="photo photo--groceries" role="img" aria-label="Photo of a delivery person holding a box of fresh groceries"></div>
    <div class="photo photo--restaurant" role="img" aria-label="Photo of a courier holding pizza boxes"></div>
  </div>
  <div class="services">
    <div class="service">
      <div class="service-icon icon--laundry" role="img" aria-label="Shirt icon"><span></span></div>
      <div class="service-name">Laundry Pickup</div>
      <div class="service-phone">+9714-382-6047</div>
    </div>
    <div class="service">
      <div class="service-icon icon--groceries" role="img" aria-label="Grocery basket icon"><span></span></div>
      <div class="service-name">Groceries Delivery</div>
      <div class="service-phone">+9714-382-6047</div>
    </div>
    <div class="service">
      <div class="service-icon icon--restaurant" role="img" aria-label="Food delivery scooter icon"><span></span></div>
      <div class="service-name">Restaurants Delivery</div>
      <div class="service-phone">+9714-382-6047</div>
    </div>
  </div>
</section>

<section class="insert insert--home">
  <div class="contact-bar"><span>Call Us 12345 48213</span><span>www.maplequarters.com</span></div>
  <div class="mood-photo" role="img" aria-label="Photo of a candlelit dinner table with a glass of rosé wine and roses"></div>
  <div class="brand brand--light">MAPLE<small>QUARTERS</small></div>
  <h1 class="script-title">Feel<span class="line2">at home</span></h1>
  <p class="quote-band">"Dim the lights, light up a candle,<br>play nice music, have a relaxing stay."</p>
</section>

</body>
</html>
```